Roofing company needs a door hanger designed.

Hello, I would like to have a door hanger designed for our roofing company in Orlando Florida. I have included information about us below and attached our logo. Please let me know if there is anything else you need? thank you.

BRIGHT HARBOR ROOFING
5417 Copper Meadow Blvd. Winter Park, FL 32795
Website: brightharborroofco.example
Email: info@brightharborroofco.example
Office phone #: 407.555.0146

Notes: In the state of Florida a roofing contractor must include their license number on all documentation and marketing materials. Lic#CCC1590827

Items I would like to add:
-CALL TODAY FOR A FREE ESTIMATE
-SCHEDULE YOUR FREE INSPECTION TODAY
-OUR SERVICES: ROOF REPLACEMENT, ROOF REPAIR, EMERGENCY SERVICES
-LICENSED & INSURED
OTHER SENTENCES / PARAGRAPHS IF NEEDED.
-We at Bright Harbor Roofing are dedicated to providing superior service.
-Driven to offer the highest quality and professional commercial and residential roofing solutions at a fair price.
-Our goal is to provide you with the best value possible!
-The best option not the highest priced option. Sometimes a small roof repair is all it takes to fix your roofing issues.
-Free roof inspections and proposals that are customized to your project to solve your roofing needs.

```html
<!DOCTYPE html>
<html lang="en">
<head>
<meta charset="utf-8">
<title>Bright Harbor Roofing – Door Hanger</title>
<link rel="stylesheet" href="https://fonts.googleapis.com/css2?family=Lato:wght@400;700;900&family=Open+Sans:wght@400;700;800&display=swap">
<style>
  :root {
    --ink: #111111;
    --white: #ffffff;
    --brand-blue: #2f5fae;
    --accent-orange: #ef5a24;
    --band-yellow: #e8c51a;
    --footer-black: #000000;
    --label-yellow: #f2c812;
  }
  * { margin: 0; padding: 0; box-sizing: border-box; }
  html, body { width: 1200px; height: 1183px; overflow: hidden; background: var(--white); }
  body { position: relative; font-family: "Lato", sans-serif; color: var(--ink); }

  .side-label {
    position: absolute; top: 76px; width: 426px; text-align: center;
    font-family: "Open Sans", sans-serif; font-size: 21px; letter-spacing: 0.5px;
  }
  .side-label--front { left: 130px; }
  .side-label--back { left: 597px; }

  .spec { position: absolute; left: 1040px; top: 262px; width: 150px; text-align: center; font-family: "Open Sans", sans-serif; }
  .spec__title { font-weight: 800; font-size: 21px; letter-spacing: 1px; }
  .spec__value { margin-top: 26px; font-size: 20px; line-height: 1.2; letter-spacing: 0.5px; }

  .hanger {
    position: absolute; width: 426px; height: 1020px;
    border: 1.5px solid var(--ink); background: var(--white); overflow: hidden;
  }
  .hanger--front { left: 130px; top: 114px; }
  .hanger--back { left: 597px; top: 112px; }

  .hanger__photo { position: absolute; left: 0; top: 0; width: 100%; height: 487px; }
  .hanger--front .hanger__photo {
    background: linear-gradient(180deg, #4f86d2 0%, #8ab4e6 30%, #c9d9ea 45%, #5a4d47 55%, #e9e3cf 68%, #2d2a28 80%, #5f7a38 92%, #4d6b2a 100%);
  }
  .hanger--back .hanger__photo {
    background: linear-gradient(180deg, #6fbfee 0%, #85c8ef 22%, #7b6f62 38%, #b7a48d 55%, #f0efea 66%, #6f5c4c 78%, #4b7d2e 90%, #3f6b25 100%);
  }

  .hanger__hole { position: absolute; inset: 0; width: 100%; height: 100%; pointer-events: none; }

  .hanger__band {
    position: absolute; left: 0; top: 487px; width: 100%; height: 46px;
    background: var(--band-yellow);
    display: flex; align-items: center; justify-content: center;
    font-family: "Lato", sans-serif; font-weight: 700; font-size: 21.5px; color: var(--ink);
  }

  .hanger__brand {
    position: absolute; left: 0; top: 560px; width: 100%; text-align: center;
    font-family: "Lato", sans-serif; font-weight: 900; color: var(--brand-blue);
    line-height: 1;
  }
  .hanger__brand-name { display: block; font-size: 43px; letter-spacing: -0.5px; }
  .hanger__brand-sub { display: block; margin-top: 10px; font-size: 26px; letter-spacing: 9px; }
  .hanger__brand-mark {
    display: block; width: 34px; height: 34px; border-radius: 50%;
    background: var(--label-yellow); margin: 0 auto 12px;
  }

  .offer { position: absolute; left: 0; top: 742px; width: 100%; }
  .offer__lead {
    text-align: center; font-family: "Lato", sans-serif; font-size: 26px;
    color: var(--brand-blue); padding-left: 0;
  }
  .offer__list { list-style: none; margin-top: 8px; padding-left: 40px; }
  .offer__item {
    font-family: "Open Sans", sans-serif; font-weight: 800; font-size: 39px;
    color: var(--accent-orange); line-height: 45px; letter-spacing: 0.3px;
  }
  .offer__item::before { content: "• "; }

  .services { position: absolute; left: 0; top: 740px; width: 100%; }
  .services__title {
    text-align: center; font-family: "Lato", sans-serif; font-size: 27px;
    color: var(--brand-blue);
  }
  .services__list { list-style: none; margin-top: 8px; padding-left: 57px; }
  .services__item {
    font-family: "Open Sans", sans-serif; font-weight: 800; font-size: 28.5px;
    color: var(--accent-orange); line-height: 35px;
  }
  .services__item::before { content: "• "; }

  .hanger__footer {
    position: absolute; left: 0; bottom: 0; width: 100%; height: 132px;
    background: var(--footer-black); color: var(--white);
    font-family: "Lato", sans-serif; font-size: 14.5px; line-height: 18px;
    padding-top: 15px; text-align: center;
  }
  .footer__cols { display: flex; justify-content: center; gap: 18px; }
  .footer__col { text-align: center; }
  .footer__heading { color: var(--label-yellow); font-weight: 700; font-size: 14.5px; }
  .footer__contact { margin-top: 7px; }
  .footer__key { color: var(--label-yellow); font-weight: 700; }
</style>
</head>
<body>

  <div class="side-label side-label--front">FRONT</div>
  <div class="side-label side-label--back">BACK</div>

  <div class="spec">
    <div class="spec__title">SIZE:</div>
    <div class="spec__value">3.5″ WIDE<br>8.5″ TALL</div>
  </div>

  <!-- Front side -->
  <section class="hanger hanger--front">
    <div class="hanger__photo" role="img" aria-label="Photo of a two-storey house with a dark shingle roof and glass porch under a blue sky with white clouds"></div>
    <svg class="hanger__hole" viewBox="0 0 426 1020" aria-hidden="true">
      <line x1="267" y1="67" x2="318" y2="0" stroke="#111" stroke-width="1.5"/>
      <circle cx="214" cy="125" r="79" fill="#fff" stroke="#111" stroke-width="1.5"/>
    </svg>
    <div class="hanger__band">brightharborroofco.example</div>

    <div class="hanger__brand">
      <span class="hanger__brand-mark"></span>
      <span class="hanger__brand-name">BRIGHT HARBOR</span>
      <span class="hanger__brand-sub">ROOFING</span>
    </div>

    <div class="offer">
      <p class="offer__lead">Call Today to Schedule Your</p>
      <ul class="offer__list">
        <li class="offer__item">FREE Estimate</li>
        <li class="offer__item">FREE Inspection</li>
      </ul>
    </div>

    <footer class="hanger__footer">
      <div class="footer__cols">
        <div class="footer__col">
          <div class="footer__heading">BRIGHT HARBOR ROOFING</div>
          <div>5417 Copper Meadow Blvd.</div>
          <div>Winter Park, FL 32795</div>
        </div>
        <div class="footer__col">
          <div class="footer__heading">LICENSED &amp; INSURED</div>
          <div>License Number</div>
          <div>CCC1590827</div>
        </div>
      </div>
      <div class="footer__contact">
        <div><span class="footer__key">EMAIL</span> info@brightharborroofco.example</div>
        <div><span class="footer__key">OFFICE PHONE</span> (407) 555-0146</div>
      </div>
    </footer>
  </section>

  <!-- Back side -->
  <section class="hanger hanger--back">
    <div class="hanger__photo" role="img" aria-label="Photo of a suburban house gable with shingle roof, white porch columns and green shrubs under a clear blue sky"></div>
    <svg class="hanger__hole" viewBox="0 0 426 1020" aria-hidden="true">
      <line x1="161" y1="67" x2="108" y2="0" stroke="#111" stroke-width="1.5"/>
      <circle cx="214" cy="125" r="79" fill="#fff" stroke="#111" stroke-width="1.5"/>
    </svg>
    <div class="hanger__band">brightharborroofco.example</div>

    <div class="hanger__brand">
      <span class="hanger__brand-mark"></span>
      <span class="hanger__brand-name">BRIGHT HARBOR</span>
      <span class="hanger__brand-sub">ROOFING</span>
    </div>

    <div class="services">
      <p class="services__title">Our Services</p>
      <ul class="services__list">
        <li class="services__item">Roof Replacement</li>
        <li class="services__item">Roof Repair</li>
        <li class="services__item">Emergency Services</li>
      </ul>
    </div>

    <footer class="hanger__footer">
      <div class="footer__cols">
        <div class="footer__col">
          <div class="footer__heading">BRIGHT HARBOR ROOFING</div>
          <div>5417 Copper Meadow Blvd.</div>
          <div>Winter Park, FL 32795</div>
        </div>
        <div class="footer__col">
          <div class="footer__heading">LICENSED &amp; INSURED</div>
          <div>License Number</div>
          <div>CCC1590827</div>
        </div>
      </div>
      <div class="footer__contact">
        <div><span class="footer__key">EMAIL</span> info@brightharborroofco.example</div>
        <div><span class="footer__key">OFFICE PHONE</span> (407) 555-0146</div>
      </div>
    </footer>
  </section>

</body>
</html>
```